Fire Hydrant Repair Parts Flyer

We need a flyer advertising both fire hydrant parts and the manufacturers that we are stocking. Our company is Coastal Flowline Supply and we are a parts distributor who sells directly to contractors. I have attached an example flyer that advertises some other parts we stock. We don't want it to look exactly like the old flyer, but we would like it to be structured similarly. I have also attached a background image for the flyer as well as some pictures of the parts we are stocking. I have also attached pictures of the manufacturer logos that we are stocking. We are trying to convey the parts that we are stocking which are: "Traffic Repair Kits", "Main Valve Repair Kits", "Extension Kits", "Replacement Caps & Gaskets", "Replacement Nozzles", Adjustable Hydrant Wrenches", "Hydrant Diffusers", & "Hydrant Oil". I have attached pictures of some of these items that we would like placed on the flyer. Let me know if you have any questions at all.

```html
<!DOCTYPE html>
<html lang="en">
<head>
<meta charset="utf-8">
<title>Fire Hydrant Repair Parts</title>
<link rel="stylesheet" href="https://fonts.googleapis.com/css2?family=Roboto+Condensed:wght@400;500;700;800&display=swap">
<style>
  :root {
    --brand-blue: #3d52a8;
    --blue-light: #5f70b3;
    --blue-deep: #33469a;
    --accent-red: #e8194f;
    --white: #ffffff;
    --ink: #222428;
  }
  * { margin: 0; padding: 0; box-sizing: border-box; }
  html, body { width: 849px; height: 1200px; overflow: hidden; background: var(--white); }
  .flyer { position: relative; width: 849px; height: 1200px; overflow: hidden; font-family: "Roboto Condensed", "Arial Narrow", sans-serif; }
  .backdrop { position: absolute; inset: 0; }
  .headline { position: absolute; left: 400px; top: 282px; width: 440px; text-align: center; }
  .headline__main { color: var(--brand-blue); font-weight: 800; font-size: 58px; line-height: 1; letter-spacing: -2px; }
  .headline__sub { color: var(--accent-red); font-weight: 700; font-size: 40px; line-height: 1; letter-spacing: 9px; margin-top: 6px; }
  .product { position: absolute; }

  .parts-list { position: absolute; left: 0; top: 776px; width: 849px; color: var(--white); font-size: 21px; font-weight: 400; letter-spacing: 0.4px; }
  .parts-row { display: flex; align-items: center; justify-content: center; gap: 22px; height: 37px; margin-bottom: 20px; white-space: nowrap; }
  .parts-row--first { padding-right: 46px; }
  .parts-row--second { padding-left: 20px; }
  .parts-row--last { margin-top: 2px; }
  .part { line-height: 33px; }
  .part--boxed { border: 2px solid var(--white); border-radius: 13px; padding: 0 26px; }
  .parts-row--first .part--boxed { padding: 0 40px; }
  .parts-row--second .part--boxed { padding: 0 28px; }
  .parts-row--third .part--boxed { padding: 0 34px; }

  .company { position: absolute; top: 1040px; left: 0; width: 849px; display: flex; justify-content: center; align-items: center; gap: 14px; }
  .company__mark { width: 22px; height: 22px; background: var(--accent-red); }
  .company__name { color: var(--brand-blue); font-size: 31px; font-weight: 400; }
  .maker-rule { position: absolute; top: 1112px; height: 4px; background: var(--brand-blue); }
  .makers { position: absolute; top: 1134px; left: 100px; width: 650px; display: flex; justify-content: space-between; align-items: center; gap: 24px; white-space: nowrap; }
  .maker { color: var(--ink); font-size: 17px; font-weight: 700; letter-spacing: 0.4px; }
</style>
</head>
<body>
<div class="flyer">
  <svg class="backdrop" width="849" height="1200" viewBox="0 0 849 1200">
    <defs>
      <linearGradient id="photoTone" x1="0" y1="0.5" x2="1" y2="0.1">
        <stop offset="0" stop-color="#b52a2e"/>
        <stop offset="0.3" stop-color="#9c9fa6"/>
        <stop offset="0.6" stop-color="#7e8792"/>
        <stop offset="1" stop-color="#8aa85a"/>
      </linearGradient>
      <linearGradient id="lensTone" x1="0" y1="0" x2="1" y2="0">
        <stop offset="0" stop-color="#6576b8"/>
        <stop offset="1" stop-color="#3a4fa5"/>
      </linearGradient>
    </defs>
    <rect class="hero-photo" role="img" aria-label="Red and silver fire hydrant with a hose attached, beside a road and grass" x="0" y="0" width="849" height="580" fill="url(#photoTone)"/>
    <rect x="0" y="600" width="849" height="520" fill="var(--brand-blue)"/>
    <path d="M0,640 L520,640 C540,780 500,920 430,1060 L0,1100 Z" fill="var(--blue-light)"/>
    <path d="M345,420 C345,260 520,202 700,200 C790,200 849,215 849,220 L849,650 C700,730 520,758 400,752 C250,745 110,700 0,665 L0,420 C120,470 250,505 345,490 Z" fill="var(--white)"/>
    <path d="M200,490 C350,405 560,390 705,425 C600,472 420,512 200,490 Z" fill="url(#lensTone)"/>
    <path d="M0,1088 C250,1005 600,1000 849,1090 L849,1200 L0,1200 Z" fill="var(--white)"/>
  </svg>

  <div class="headline">
    <div class="headline__main">FIRE HYDRANT</div>
    <div class="headline__sub">REPAIR PARTS</div>
  </div>

  <div class="product" role="img" aria-label="Yellow hydrant diffuser with pressure gauge" style="left:14px;top:505px;width:108px;height:160px;border-radius:30px 30px 14px 14px;background:linear-gradient(160deg,#f2b81e,#d89a10 60%,#6c6a66);"></div>
  <div class="product" role="img" aria-label="Traffic repair kit with breakaway flange, bolts and gaskets" style="left:150px;top:568px;width:156px;height:138px;border-radius:50% 50% 20px 20px;background:linear-gradient(180deg,#2a2b2e,#4a4c52 60%,#c6c9ce);"></div>
  <div class="product" role="img" aria-label="Adjustable hydrant wrench" style="left:345px;top:566px;width:80px;height:164px;border-radius:20px;background:linear-gradient(200deg,#d6d9de,#9ea3aa);"></div>
  <div class="product" role="img" aria-label="Bottle of lightweight hydrant oil" style="left:471px;top:536px;width:64px;height:184px;border-radius:14px 14px 8px 8px;background:linear-gradient(180deg,#1e1e1e 0 8%,#eceff2 8%,#d9dde2);"></div>
  <div class="product" role="img" aria-label="Red replacement hydrant cap with chain" style="left:572px;top:530px;width:150px;height:142px;border-radius:40% 40% 30% 30%;background:linear-gradient(180deg,#c8202a 0 40%,#c9ccd1 40%,#eef0f2);"></div>
  <div class="product" role="img" aria-label="Hydrant extension kit with barrel, stem and bolts" style="left:702px;top:456px;width:134px;height:120px;border-radius:18px;background:linear-gradient(180deg,#222326,#44464b 60%,#c4c7cc);"></div>

  <div class="parts-list">
    <div class="parts-row parts-row--first">
      <span class="part part--boxed">TRAFFIC REPAIR KITS</span>
      <span class="part">MAIN VALVE REPAIR KITS</span>
    </div>
    <div class="parts-row parts-row--second">
      <span class="part">REPLACEMENT CAPS &amp; GASKETS</span>
      <span class="part part--boxed">EXTENSION KITS</span>
    </div>
    <div class="parts-row parts-row--third">
      <span class="part part--boxed">ADJUSTABLE HYDRANT WRENCHES</span>
      <span class="part">REPLACEMENT NOZZLES</span>
    </div>
    <div class="parts-row parts-row--last">
      <span class="part">HYDRANT DIFFUSERS &amp; HYDRANT OIL</span>
    </div>
  </div>

  <div class="company">
    <span class="company__mark"></span>
    <span class="company__name">Coastal Flowline Supply</span>
  </div>

  <div class="maker-rule" style="left:88px;width:265px;"></div>
  <div class="maker-rule" style="left:460px;width:263px;"></div>

  <div class="makers">
    <span class="maker">Harlow</span>
    <span class="maker">Ridgeline Pipe</span>
    <span class="maker">Brannock Valve</span>
    <span class="maker">Tidewater Valve</span>
    <span class="maker">Stellan Valve Co.</span>
  </div>
</div>
</body>
</html>
```